Breezeway Comfort business cards design

Need a business card design for a Heating and Air Conditioning business. I need these items included.
Business name: Breezeway Comfort
Owner: Dalton Fairbrook
License # 2748519
Phone number # 555-382-4067
Email: breezewaycomfortair@mailnest.example
Sales
Service
Installation
Maintenance

Heating and Air Conditioning

Requirements
Must have
• Company name , license number , phone number , email

```html
<!DOCTYPE html>
<html lang="en">
<head>
<meta charset="utf-8">
<title>Breezeway Comfort business cards</title>
<link rel="stylesheet" href="https://fonts.googleapis.com/css2?family=Exo+2:wght@400;500;600&display=swap">
<style>
  :root {
    --backdrop: #c3cbe0;
    --card-blue: #0a3ca6;
    --paper: #ffffff;
    --accent-orange: #f7883a;
    --accent-red: #e8385a;
    --text-light: #ffffff;
    --rule: rgba(255,255,255,0.55);
  }
  * { margin: 0; padding: 0; box-sizing: border-box; }
  html, body { width: 1200px; height: 900px; overflow: hidden; }
  body {
    background: var(--backdrop);
    font-family: "Exo 2", sans-serif;
    position: relative;
  }
  .card {
    position: absolute;
    left: 330px;
    width: 558px;
    height: 342px;
    border-radius: 42px 0 42px 0;
    overflow: hidden;
  }
  .card--front { top: 92px; background: var(--paper); }
  .card--back { top: 470px; background: var(--card-blue); }

  .front-shape { position: absolute; inset: 0; }

  .brand-mark {
    position: absolute;
    left: 28px;
    top: 152px;
    display: flex;
    align-items: center;
    gap: 10px;
  }
  .brand-mark__dot {
    width: 16px; height: 16px; border-radius: 50%;
    background: var(--accent-orange);
  }
  .brand-mark__name {
    font-weight: 600;
    font-size: 19px;
    color: var(--card-blue);
    letter-spacing: 0.4px;
  }

  .contact {
    position: absolute;
    right: 26px;
    text-align: right;
    color: var(--text-light);
    white-space: nowrap;
  }
  .contact__name {
    top: 74px;
    font-size: 16px;
    font-weight: 500;
    letter-spacing: 1.2px;
  }
  .contact__role {
    top: 94px;
    font-size: 13px;
    letter-spacing: 1px;
    color: var(--accent-orange);
  }
  .contact__license { top: 166px; font-size: 15px; }
  .contact__line {
    font-size: 15px;
    display: flex;
    align-items: center;
    justify-content: flex-end;
    gap: 6px;
  }
  .contact__phone { top: 203px; }
  .contact__email { top: 225px; font-size: 12.5px; letter-spacing: -0.1px; }
  .contact__line svg { width: 15px; height: 15px; flex: none; }

  .rule {
    position: absolute;
    left: 325px; right: 26px; top: 271px;
    height: 1px; background: var(--rule);
  }
  .services {
    position: absolute;
    right: 26px; top: 278px;
    display: grid;
    grid-template-columns: auto auto;
    column-gap: 16px;
    row-gap: 2px;
    color: var(--text-light);
    font-size: 15px;
  }
  .services li {
    list-style: none;
    display: flex;
    align-items: center;
    justify-content: flex-end;
    gap: 6px;
  }
  .services li::after {
    content: "";
    width: 8px; height: 8px; border-radius: 50%;
    background: var(--accent-orange);
  }

  .back-brand {
    position: absolute;
    left: 0; right: 0; top: 132px;
    display: flex;
    flex-direction: column;
    align-items: center;
    gap: 18px;
  }
  .back-brand__dot {
    width: 30px; height: 30px; border-radius: 50%;
    background: var(--accent-orange);
  }
  .back-brand__name {
    font-weight: 600;
    font-size: 40px;
    letter-spacing: 2px;
    color: var(--accent-orange);
    text-transform: uppercase;
  }
</style>
</head>
<body>
  <section class="card card--front">
    <svg class="front-shape" viewBox="0 0 558 342" preserveAspectRatio="none" aria-hidden="true">
      <defs>
        <linearGradient id="sweep" x1="0" y1="0" x2="0" y2="1">
          <stop offset="0" stop-color="#f7883a"/>
          <stop offset="1" stop-color="#e8385a"/>
        </linearGradient>
      </defs>
      <path d="M302 0 C 322 70, 300 150, 255 215 C 225 265, 212 300, 205 342 L 558 342 L 558 0 Z" fill="url(#sweep)"/>
      <path d="M336 0 C 340 80, 318 160, 275 220 C 245 265, 228 305, 210 342 L 558 342 L 558 0 Z" fill="#0a3ca6"/>
    </svg>

    <div class="brand-mark">
      <span class="brand-mark__dot"></span>
      <span class="brand-mark__name">Breezeway Comfort</span>
    </div>

    <p class="contact contact__name">DALTON FAIRBROOK</p>
    <p class="contact contact__role">OWNER</p>
    <p class="contact contact__license">License # 2748519</p>
    <p class="contact contact__line contact__phone">555-382-4067
      <svg viewBox="0 0 24 24" aria-hidden="true"><path fill="#f7883a" d="M6.6 10.8a15.1 15.1 0 0 0 6.6 6.6l2.2-2.2a1 1 0 0 1 1-.25 11.4 11.4 0 0 0 3.6.57 1 1 0 0 1 1 1V20a1 1 0 0 1-1 1A17 17 0 0 1 3 4a1 1 0 0 1 1-1h3.5a1 1 0 0 1 1 1c0 1.25.2 2.45.57 3.57a1 1 0 0 1-.25 1z"/></svg>
    </p>
    <p class="contact contact__line contact__email">breezewaycomfortair@mailnest.example
      <svg viewBox="0 0 24 24" aria-hidden="true"><rect x="2" y="5" width="20" height="14" rx="1.5" fill="#f7883a"/><path d="M3 6l9 7 9-7" fill="none" stroke="#0a3ca6" stroke-width="1.6"/></svg>
    </p>

    <div class="rule"></div>
    <ul class="services">
      <li>Sales</li>
      <li>Installation</li>
      <li>Service</li>
      <li>Maintenance</li>
    </ul>
  </section>

  <section class="card card--back">
    <div class="back-brand">
      <span class="back-brand__dot"></span>
      <span class="back-brand__name">Breezeway Comfort</span>
    </div>
  </section>
</body>
</html>
```